Professional business podcast cover

Hey guys,

I want to redesign my podcast cover from the Vimpa Podcast.

It is a professional business podcast for small and medium sized business. Therefor I need something professional.
No fancy glitter designs.
Something real clean and easy.

I am thinking about something similar to this pic.
https://snapvault.example/7Qk2Lm9xP4aZ

What is important for the design?

1. professional and clean look
2. fonts= roboto
3. the logo must be readable also on small devices (please do not change the existing logo!)
4. same color as the logo
5. my full name must be included in the design: Joss Belder

Thank you for your work.

I can not wait to get your designs.

Regards

Joss from Vimpa

Reason: I need a perfect fitting timeless design. If it needs more time to be generated, than we do so.

Target Market(s)

Small and medium sized CEOs

Industry/Entity Type

Consulting

Font styles to use
Sans Serif

Colors
acd136

Requirements
Must have
• 1. professional and clean look
• 2. fonts= roboto
• 3. the logo must be readable also on small devices
• 4. same color as the logo
• 5. size 1400x 1400
• 6. Text: Joss Belder very present
Nice to have
• Get inspired by covers like Dale Korvin, Gus Pellmore or Neil Ostrands podcast.
• https://snapvault.example/4Rb8Tn2wQ6cY
• https://snapvault.example/9Hd3Vj5sK1eX
• https://snapvault.example/2Mf6Pw8uL3gW
Should not have
• Fancy glossi shinny designs

```html
<!DOCTYPE html>
<html lang="de">
<head>
<meta charset="utf-8">
<title>Vimpa Podcast Cover</title>
<link href="https://fonts.googleapis.com/css2?family=Open+Sans:wght@400;600&family=Roboto:wght@700&display=swap" rel="stylesheet">
<style>
  :root {
    --stage: #161616;
    --cover: #000000;
    --tile: #1c1c1c;
    --brand-green: #22c31a;
    --brand-green-light: #8fdc80;
    --text-light: #ffffff;
    --photo-top: #3a2e28;
    --photo-bottom: #15181d;
  }
  html, body {
    margin: 0;
    padding: 0;
    width: 1200px;
    height: 741px;
    overflow: hidden;
    background: var(--stage);
  }
  .cover {
    position: absolute;
    left: 270px;
    top: 40px;
    width: 660px;
    height: 660px;
    background: var(--cover);
    overflow: hidden;
  }
  .checker-tile {
    position: absolute;
    width: 132px;
    height: 110px;
    background: var(--tile);
  }
  .portrait {
    position: absolute;
    left: 188px;
    top: 84px;
    width: 453px;
    height: 555px;
    background: linear-gradient(180deg, var(--photo-top) 0%, #242228 45%, var(--photo-bottom) 100%);
    clip-path: polygon(40% 0, 72% 0, 78% 30%, 100% 52%, 100% 100%, 0 100%, 8% 62%, 38% 48%, 36% 28%);
  }
  .frame {
    position: absolute;
    inset: 16px;
    border: 5px solid var(--brand-green);
    pointer-events: none;
  }
  .brand {
    position: absolute;
    left: 48px;
    top: 66px;
    display: flex;
    align-items: center;
    gap: 12px;
  }
  .brand-dot {
    width: 62px;
    height: 62px;
    border-radius: 50%;
    background: var(--brand-green-light);
  }
  .brand-name {
    font-family: "Open Sans", sans-serif;
    font-weight: 600;
    font-size: 84px;
    line-height: 1;
    color: var(--brand-green);
    letter-spacing: -1px;
  }
  .tagline {
    position: absolute;
    left: 40px;
    top: 176px;
    width: 320px;
    margin: 0;
    text-align: center;
    font-family: "Open Sans", sans-serif;
    font-size: 25px;
    line-height: 31px;
    color: var(--text-light);
  }
  .name-band {
    position: absolute;
    left: 26px;
    top: 522px;
    width: 548px;
    height: 96px;
    background: var(--brand-green);
    display: flex;
    align-items: center;
    justify-content: center;
    padding-right: 90px;
    box-sizing: border-box;
  }
  .host-name {
    margin: 0;
    font-family: "Roboto", sans-serif;
    font-weight: 700;
    font-size: 45px;
    letter-spacing: 0.5px;
    color: var(--text-light);
    text-transform: uppercase;
  }
</style>
</head>
<body>
  <main class="cover">
    <div class="checker-tile" style="left:420px; top:48px;"></div>
    <div class="checker-tile" style="left:540px; top:158px;"></div>
    <div class="checker-tile" style="left:20px; top:290px;"></div>
    <div class="checker-tile" style="left:264px; top:290px;"></div>
    <div class="checker-tile" style="left:132px; top:400px;"></div>
    <div class="checker-tile" style="left:132px; top:200px;"></div>

    <div class="portrait" role="img" aria-label="Portrait of the host in a dark suit, white shirt and dark tie"></div>

    <div class="brand">
      <span class="brand-dot"></span>
      <span class="brand-name">Vimpa</span>
    </div>
    <p class="tagline">Unternehmerwissen<br>umsetzbar in 15 Minuten</p>

    <div class="name-band">
      <h1 class="host-name">Joss Belder</h1>
    </div>

    <div class="frame"></div>
  </main>
</body>
</html>
```